Non profit Haiti relief organization needs an invitation to a fundraising event

We need a catchy invitation for our 8th annual "Light the Lantern Path" event. Our mission is to provide relief, hope and dignity to the poor, elderly and homeless people of Haiti. This direct mail piece will measure 5 x 7 and will be mailed to 3,000 supports and used for personal invitation. The invitation needs to include a photo of a wheel that we use every year, a photo of our founder, the late Fr. Lucien Dovale, one or two photos of the poor that we serve in Haiti, and our logo. I uploaded some photos, but photos from our website could also be used.

Text:
Providing relief, hope & dignity to the poor, elderly & homeless people of Haiti.
Education, Water, Food, Orphan Care, Elder Care

8th Annual "Light The Lantern Path" Event
Wednesday, April 23, 2014 6pm
Gardens of Pellham, 20817 Colby Ave NE, Pellham, MN

Live Auction, Marketplace, Music, Beverages, Appetizers

$5 Admission. Pay at the door.

Help us carry on Father Dovale's legacy in Haiti.

www.lanternaidhouse.org 555-014-7298

Dovale Mercy, Inc. is a 501(c)(3) non-profit organization. All donations tax deductible.

Target Market(s)

Adults who live in Minnesota, Christians

Industry/Entity Type

Non-Profit

Requirements
Must have
• The invitation must be 5 x 7 and have print on both sides. Must have text listed in project overview
Nice to have
• I included front and back images of the postcard that we used last year to give an idea of design that we've used in past.

```html
<!DOCTYPE html>
<html lang="en">
<head>
<meta charset="utf-8">
<title>Light the Lantern Path – Invitation</title>
<link href="https://fonts.googleapis.com/css2?family=EB+Garamond:ital,wght@0,400;0,600;0,700;1,400;1,600;1,700&family=Montserrat:wght@700;800&display=swap" rel="stylesheet">
<style>
:root{
  --teal:#2fb5b0;
  --ink:#111;
  --paper:#fff;
  --frame:#b9c4c3;
  --photo-turquoise:#4fb6b3;
  --photo-skin:#6b4230;
  --photo-sky:#8cc3c9;
  --photo-wood:#9b8a6a;
}
*{box-sizing:border-box;margin:0;padding:0}
html,body{width:1200px;height:1000px;overflow:hidden;background:var(--paper)}
body{position:relative;font-family:"EB Garamond",Georgia,serif;color:var(--ink)}
.card{position:absolute;left:248px;width:676px;height:482px;border:1px solid #555;overflow:hidden;background:var(--paper)}
.card--front{top:12px}
.card--back{top:505px}
.abs{position:absolute}
.center{text-align:center}
h1,h2{font-weight:400}

/* front */
.front-hero{left:0;top:0;width:309px;height:482px;background:linear-gradient(160deg,var(--photo-turquoise),#2b8f8c 45%,var(--photo-skin) 80%,#2a2320)}
.front-edge{right:4px;top:0;width:4px;height:482px;background:var(--teal)}
.front-panel{left:309px;top:0;width:362px;height:482px}
.tagline{top:6px;left:0;width:100%;font-style:italic;font-size:17.5px;line-height:21px}
.headline{top:44px;left:0;width:100%;font-size:84px;line-height:74px;letter-spacing:-1px}
.headline-sub{top:110px;left:0;width:100%;font-size:52px;line-height:52px}
.photo-frame{left:50px;top:160px;width:253px;height:190px;border:2px solid var(--frame);padding:3px;display:flex;gap:3px}
.photo-frame .photo{flex:1;height:100%}
.photo--elder{background:linear-gradient(135deg,#6d6a55,#4a3a33 50%,#7a8ea4)}
.photo--woman{background:linear-gradient(160deg,#88a9a4,#5b3d2c 55%,#d9c24a)}
.annual{top:350px;left:0;width:100%;font-size:44px;line-height:46px}
.annual sup{font-size:26px;vertical-align:14px}
.event-name{top:396px;left:0;width:100%;font-style:italic;font-weight:700;font-size:19px;line-height:24px}
.event-list{top:421px;left:0;width:100%;font-style:italic;font-weight:600;font-size:13.5px;line-height:18px}
.brand-name{font-family:"EB Garamond",Georgia,serif;font-weight:600;color:var(--ink)}
.front-brand{top:448px;left:0;width:100%;font-size:19px;line-height:24px}

/* back */
.back-hero{left:0;top:0;width:676px;height:200px;background:linear-gradient(100deg,#5b5450 0%,var(--photo-sky) 30%,#7fc59a 55%,var(--photo-sky) 75%,var(--photo-wood))}
.mission-band{left:0;top:200px;width:527px;height:70px;background:var(--teal)}
.mission-title{left:24px;top:198px;font-size:62px;line-height:60px;letter-spacing:-0.5px}
.mission-list{left:150px;top:251px;width:350px;text-align:right;font-family:"Montserrat",Arial,sans-serif;font-weight:700;font-size:12.5px;color:#1d2b2b}
.photo--founder{left:527px;top:200px;width:130px;height:173px;background:linear-gradient(180deg,#e9e7e4,#b9a79a 55%,#1d1d1f 85%)}
.photo--child{left:22px;top:253px;width:104px;height:97px;background:linear-gradient(150deg,#d7c9b6,#5e3f2e 60%,#e5e1d6)}
.photo--grandfather{left:22px;top:350px;width:104px;height:101px;background:linear-gradient(180deg,#a49d95,#4d3a30 55%,#d23b3b)}
.invite{left:130px;top:272px;width:400px}
.invite-lead,.invite-date{font-weight:700;font-size:25px;line-height:29px}
.invite-fee{font-weight:700;font-size:19px;line-height:24px;margin-top:2px}
.invite-venue{font-style:italic;font-size:18px;line-height:20px}
.back-brand{left:130px;top:398px;width:400px;font-size:24px;line-height:30px}
.legal{left:125px;top:437px;width:400px;font-family:"Montserrat",Arial,sans-serif;font-size:7px}
.legacy{left:515px;top:377px;width:160px;font-style:italic;font-size:16px;line-height:20px}
.footer-bar{left:0;top:452px;width:676px;height:30px;background:#000;color:#fff;font-family:"Montserrat",Arial,sans-serif;font-weight:800;font-size:17px;letter-spacing:2px;line-height:30px;word-spacing:4px}
</style>
</head>
<body>

<section class="card card--front">
  <div class="abs front-hero" role="img" aria-label="Photo of a young Haitian girl holding a bag against a turquoise wall"></div>
  <div class="abs front-panel">
    <p class="abs tagline center">Providing relief, hope &amp; dignity to the poor,<br>elderly &amp; homeless people of Haiti.</p>
    <h1 class="abs headline center">SPREAD</h1>
    <p class="abs headline-sub center">THE WORD</p>
    <div class="abs photo-frame">
      <div class="photo photo--elder" role="img" aria-label="Photo of an elderly woman praying with a rosary"></div>
      <div class="photo photo--woman" role="img" aria-label="Photo of a smiling woman carrying a basin on her head"></div>
    </div>
    <p class="abs annual center">8<sup>TH</sup> ANNUAL</p>
    <p class="abs event-name center">“Light the Lantern Path” Event</p>
    <p class="abs event-list center">Live Auction, Marketplace, Music, Beverages, Appetizers</p>
    <p class="abs front-brand center brand-name">Dovale Mercy Inc</p>
  </div>
  <div class="abs front-edge"></div>
</section>

<section class="card card--back">
  <div class="abs back-hero" role="img" aria-label="Photo of a volunteer sharing a camera with laughing children"></div>
  <div class="abs mission-band"></div>
  <h2 class="abs mission-title">OUR MISSION</h2>
  <p class="abs mission-list">Education, Water, Food, Orphan Care, Elder Care</p>
  <div class="abs photo--founder" role="img" aria-label="Portrait of the founder, Fr. Lucien Dovale"></div>
  <div class="abs photo--child" role="img" aria-label="Photo of a volunteer holding a small child"></div>
  <div class="abs photo--grandfather" role="img" aria-label="Photo of a smiling elderly man"></div>
  <div class="abs invite center">
    <p class="invite-lead">Please Join Us on…</p>
    <p class="invite-date">Wednesday, April 23, 2014 &nbsp;•&nbsp; 6pm</p>
    <p class="invite-fee">$5 Admission. Pay at the door.</p>
    <p class="invite-venue">Gardens of Pellham,<br>20817 Colby Ave NE, Pellham, MN</p>
  </div>
  <p class="abs back-brand center brand-name">Dovale Mercy Inc</p>
  <p class="abs legal center">Dovale Mercy, Inc. is a 501(c)(3) non-profit organization. All donations tax deductible.</p>
  <p class="abs legacy center">Help us carry on<br>Father Dovale's<br>legacy in Haiti.</p>
  <p class="abs footer-bar center">www.lanternaidhouse.org &nbsp;| &nbsp;555-014-7298</p>
</section>

</body>
</html>
```